Create a Graphic About YOURSELF and PixelHarbor

PixelHarbor would like you (designers) to create an awesome graphic to promote YOURSELF and your profile on PixelHarbor!

Your graphic should communicate your name, your services and should mention PixelHarbor.

The design should be perfect for sharing on Chatterly. Here's an example of what we'd like http://blog.pixelharbor-example.ca/article/333/pixelharbor-launches-3000-hire-me-social-design-contest

Once you submitted your design, we'd love you to share the design ('advertisement') and promote yourself and PixelHarbor to your friends and potential customers. So make your submissions great and get your friends to vote for your design by 'Liking' it on Chatterly!

Prizes:
$1500 - "PixelHarbor Community" prize awarded to the designer with the most Chatterly 'Likes'
5 x $50 for the next 5 'most liked' designs on Chatterly

$1000 - "Hire Me" prize awarded to the designer who receives the most client invites
5 x $50 for the next 5 'most invited' designers

In summary, this is a great opportunity for you to increase your exposure to PixelHarbor customers and win cash prizes. Show off your design skills and get hired by PixelHarbor customers from around the world!

Target Market(s)

Fans, friends and customers of YOU

Industry/Entity Type

Cash

Requirements
Must have
• 1) Include your PixelHarbor user name on the graphic so customers can find you in the PixelHarbor Designer Directory
2) Include the tagline "Hire Me on PixelHarbor.com!" in your graphic design.
3) Share your design's URL on our Chatterly wall at http://chatterly-example.com/pixelharbor and get your friends to 'like' your design.
Nice to have
• 1) Include a tagline that expresses your design approach/philosophy
2) Artwork dimensions: 403 x 403 px
3) You can submit more than 1 design!
Should not have
• You must own the copyright of any images you use including stock imagery.

```html
<!DOCTYPE html>
<html lang="en">
<head>
<meta charset="utf-8">
<title>Hire Me on PixelHarbor.com!</title>
<link rel="stylesheet" href="https://fonts.googleapis.com/css2?family=Rubik+Distressed&family=Permanent+Marker&family=Libre+Baskerville:wght@400;700&family=Arimo:wght@400&display=swap">
<style>
  :root {
    --ink: #000000;
    --paper: #ffffff;
    --band-light: #ffffff;
    --band-mid: #e2e2e2;
    --band-dark: #9e9e9e;
    --magenta: #e3198f;
    --hot-pink: #ee1fb4;
    --sky: #1e95d0;
    --slate: #4b5561;
    --frame: #9aa3ab;
  }
  html, body {
    margin: 0;
    padding: 0;
    overflow: hidden;
    background: var(--ink);
  }
  .poster {
    position: relative;
    width: 1200px;
    height: 1200px;
    overflow: hidden;
    background: var(--ink);
  }
  .poster__backdrop {
    position: absolute;
    inset: 0;
    width: 1200px;
    height: 1200px;
  }
  .headline-count {
    position: absolute;
    left: 20px;
    top: 0;
    width: 1160px;
    margin: 0;
    font-family: "Rubik Distressed", "Impact", sans-serif;
    font-weight: 400;
    font-size: 172px;
    line-height: 200px;
    letter-spacing: 6px;
    color: var(--paper);
    text-align: center;
    white-space: nowrap;
  }
  .role-tag {
    position: absolute;
    left: 222px;
    top: 238px;
    width: 732px;
    height: 66px;
    margin: 0;
    font-family: "Libre Baskerville", Georgia, serif;
    font-weight: 700;
    font-size: 40px;
    line-height: 66px;
    color: var(--paper);
    text-align: center;
    letter-spacing: 1px;
  }
  .tagline {
    position: absolute;
    left: 0;
    top: 368px;
    width: 1200px;
    margin: 0;
    font-family: "Libre Baskerville", Georgia, serif;
    font-weight: 400;
    font-size: 100px;
    line-height: 120px;
    color: var(--ink);
    text-align: center;
    white-space: nowrap;
    letter-spacing: -1px;
  }
  .tagline strong { font-weight: 700; }
  .byline {
    position: absolute;
    left: 0;
    top: 500px;
    width: 1200px;
    margin: 0;
    font-family: "Arimo", Arial, sans-serif;
    font-size: 40px;
    line-height: 48px;
    color: var(--ink);
    text-align: center;
  }
  .burst-area {
    position: absolute;
    left: 530px;
    top: 540px;
    width: 690px;
    height: 640px;
    border-radius: 50%;
    background: radial-gradient(circle at 55% 55%, var(--sky) 0%, rgba(30,149,208,0.55) 45%, rgba(30,149,208,0) 72%);
  }
  .hire-call {
    position: absolute;
    left: 26px;
    top: 770px;
    width: 480px;
    margin: 0;
    font-family: "Permanent Marker", "Comic Sans MS", cursive;
    font-weight: 400;
    color: var(--hot-pink);
    transform: rotate(-6deg);
    transform-origin: left top;
  }
  .hire-call__line {
    display: block;
    line-height: 118px;
  }
  .hire-call__big { font-size: 118px; }
  .hire-call__small { font-size: 64px; }
  .hire-call__bang {
    font-size: 150px;
    display: inline-block;
    transform: rotate(14deg);
  }
  .brand-box {
    position: absolute;
    left: 40px;
    top: 1047px;
    width: 491px;
    height: 107px;
    box-sizing: border-box;
    background: var(--paper);
    border: 2px solid var(--frame);
    display: flex;
    align-items: center;
    justify-content: center;
    gap: 18px;
  }
  .brand-box__dot {
    width: 46px;
    height: 46px;
    border-radius: 50%;
    background: var(--sky);
  }
  .brand-box__name {
    font-family: "Arimo", Arial, sans-serif;
    font-weight: 400;
    font-size: 58px;
    color: var(--slate);
    letter-spacing: -1px;
  }
</style>
</head>
<body>
  <main class="poster">
    <svg class="poster__backdrop" viewBox="0 0 1200 1200" aria-hidden="true">
      <defs>
        <linearGradient id="band-shade" x1="0" y1="0" x2="0" y2="1">
          <stop offset="0" stop-color="var(--band-dark)"/>
          <stop offset="0.35" stop-color="var(--band-light)"/>
          <stop offset="0.6" stop-color="var(--band-light)"/>
          <stop offset="1" stop-color="var(--band-dark)"/>
        </linearGradient>
      </defs>
      <polygon class="backdrop__band" points="0,300 1200,214 1200,629 514,600 0,757" fill="url(#band-shade)"/>
      <polygon class="backdrop__role-flag" points="222,246 954,238 944,304 232,302" fill="var(--magenta)"/>
    </svg>

    <h1 class="headline-count">OVER 77,711</h1>
    <p class="role-tag">GRAPHIC DESIGNER</p>
    <p class="tagline">i’m <strong>ONE</strong> of them...</p>
    <p class="byline">by lumenform</p>

    <div class="burst-area" role="img" aria-label="Large blue decorative burst of the brand"></div>

    <p class="hire-call">
      <span class="hire-call__line hire-call__big">Hire</span>
      <span class="hire-call__line"><span class="hire-call__big">Me</span><span class="hire-call__small">on</span><span class="hire-call__bang">!</span></span>
    </p>

    <div class="brand-box">
      <span class="brand-box__dot"></span>
      <span class="brand-box__name">PixelHarbor</span>
    </div>
  </main>
</body>
</html>
```